Real Estate investment company needs billboard designs

This is our website: https://velmarkpropertygroup.com/
We are looking for some billboard concepts that uses our CEO in the design. I have attached some images and 1 billboard design that someone in our industry uses, but we don't want it exactly like his.

Industry/Entity Type

real estate

Colors

Designer to choose colors to be used in the design.

Requirements
Must have
• Company colors from websiute

```html
<!DOCTYPE html>
<html lang="en">
<head>
<meta charset="utf-8">
<title>Velmark Property Group – Guaranteed Offer Billboard</title>
<link rel="stylesheet" href="https://fonts.googleapis.com/css2?family=Bebas+Neue&family=Poppins:wght@600&display=swap">
<style>
  :root {
    --page-bg: #dcdcdc;
    --brand-red: #e10d12;
    --brand-navy: #1d1b3d;
    --white: #ffffff;
  }
  html, body {
    margin: 0;
    padding: 0;
    width: 1031px;
    height: 1200px;
    overflow: hidden;
    background: var(--page-bg);
  }
  .billboard {
    position: absolute;
    left: 35px;
    top: 378px;
    width: 960px;
    height: 444px;
    box-shadow: 0 8px 22px rgba(0, 0, 0, 0.35);
  }
  .billboard svg {
    display: block;
    width: 100%;
    height: 100%;
  }
  .headline {
    font-family: "Bebas Neue", "Oswald", sans-serif;
    font-size: 205px;
    fill: var(--white);
  }
  .headline-echo {
    font-family: "Bebas Neue", "Oswald", sans-serif;
    font-size: 205px;
    fill: none;
    stroke: var(--white);
    stroke-width: 1.5;
  }
  .company-name {
    font-family: "Poppins", sans-serif;
    font-weight: 600;
    font-size: 40px;
    fill: var(--white);
  }
  .web-address {
    font-family: "Poppins", sans-serif;
    font-weight: 600;
    font-size: 30px;
    fill: var(--white);
  }
</style>
</head>
<body>
  <main class="billboard">
    <svg viewBox="0 0 1492 690" xmlns="http://www.w3.org/2000/svg" aria-labelledby="billboard-title">
      <title id="billboard-title">Guaranteed offer billboard for Velmark Property Group</title>
      <defs>
        <linearGradient id="red-field" x1="0" y1="0" x2="1" y2="1">
          <stop offset="0" stop-color="#f0141a"/>
          <stop offset="0.55" stop-color="#d60c11"/>
          <stop offset="1" stop-color="#b3090d"/>
        </linearGradient>
        <linearGradient id="portrait-fill" x1="0" y1="0" x2="0" y2="1">
          <stop offset="0" stop-color="#c9b3a4"/>
          <stop offset="0.35" stop-color="#b9c6d8"/>
          <stop offset="1" stop-color="#8fa4c0"/>
        </linearGradient>
      </defs>

      <rect class="house-backdrop" role="img" aria-label="Red-tinted photograph of a large house" x="0" y="0" width="1492" height="690" fill="url(#red-field)"/>

      <g class="headline-echoes" opacity="0.45">
        <text class="headline-echo" x="70" y="250">GUARANTEED</text>
        <text class="headline-echo" x="70" y="440">OFFER</text>
      </g>

      <path class="white-sweep" fill="var(--white)"
            d="M0 470 C 320 450, 640 488, 960 470 C 1180 458, 1360 440, 1492 430 L1492 690 L0 690 Z"/>
      <path class="navy-field" fill="var(--brand-navy)"
            d="M0 488 C 320 470, 640 508, 960 490 C 1180 478, 1360 462, 1492 452 L1492 690 L0 690 Z"/>

      <text class="headline" x="70" y="220">GUARANTEED</text>
      <text class="headline" x="70" y="410">OFFER</text>

      <rect class="ceo-portrait" role="img" aria-label="Photograph of the company CEO smiling with arms spread wide, wearing a light denim shirt"
            x="990" y="60" width="440" height="630" rx="40" fill="url(#portrait-fill)"/>

      <text class="company-name" x="70" y="585">Velmark</text>
      <text class="company-name" x="70" y="635">Property Group</text>

      <g class="web-link">
        <circle cx="468" cy="624" r="15" fill="var(--brand-red)"/>
        <g fill="none" stroke="var(--white)" stroke-width="2">
          <ellipse cx="468" cy="624" rx="6" ry="13"/>
          <line x1="455" y1="624" x2="481" y2="624"/>
        </g>
        <text class="web-address" x="496" y="635">velmarkpropertygroup.com</text>
      </g>
    </svg>
  </main>
</body>
</html>
```